Travel Group 'Halvard Group' needs a new business card design

Halvard Group is a diverse business specialising in bespoke, tailor made holidays to suit all budgets and we are specialists in planning exciting day/short trips to suit all markets. Our target market is very varied going from the corporate client and as well as people in the community who simply want to experience something special.
We are looking for a card design that will encourage people to look at our websites and social media platforms and to see for themselves the different facets to our business. It is essential that the card has social media icons for Pagebloom, Quibbly and Snapverse. We are looking for a card with a blank background with no pictures and for the front side to have the attached Halvard logo. The card should have similar colour scheme to the attached Halvard logo.
The card must have the following information on one side:
Maren Doyle
Business Development Manager
marendoyle@halvardtravel.example
Halvard Group, 48 Fenwick Row
Kilwinning, Ayrshire, Scotland KB27 4RT
+44 (0)1632 960418
And then the card must have the following on the second side:
(Halvard logo)
(social media icons)
www.halvardtravel.example
www.halvardexperience.example
Target Market(s)
Our target market is very varied going from the corporate client and as well as people in the community who simply want to experience something special.
Industry/Entity Type
Business
Contact Information for Business Card
Maren Doyle
+44 (0)1632 960418
(Halvard logo)
(social media icons)
www.halvardtravel.example
www.halvardexperience.example
Requirements
Must have
- It is essential that the card has social media icons for Pagebloom, Quibbly & Snapverse.
Should not have
- Should not have any images other than Halvard logo.

```html
<!DOCTYPE html>
<html lang="en">
<head>
<meta charset="utf-8">
<title>Halvard Group — Business Card</title>
<link rel="stylesheet" href="https://fonts.googleapis.com/css2?family=Montserrat:wght@400;500;600;700&display=swap">
<style>
  :root {
    --backdrop: #3a3531;
    --navy: #2a2466;
    --pink: #e0409a;
    --purple: #6a3fa8;
    --ink: #4a4a4a;
    --white: #ffffff;
    --font: "Montserrat", sans-serif;
  }
  * { box-sizing: border-box; margin: 0; padding: 0; }
  html, body {
    width: 1200px; height: 930px; overflow: hidden;
    background: var(--backdrop);
    font-family: var(--font);
  }
  .card {
    position: absolute;
    width: 560px; height: 320px;
    border-radius: 16px;
    overflow: hidden;
    box-shadow: 0 10px 30px rgba(0,0,0,.35);
  }
  /* Logo side */
  .card--logo-side {
    left: 70px; top: 90px;
    background: var(--navy);
    color: var(--white);
    display: flex; flex-direction: column; align-items: center; justify-content: center;
  }
  .brand {
    display: flex; align-items: center; gap: 14px;
    font-weight: 700; letter-spacing: 4px;
  }
  .brand__dot { border-radius: 50%; flex: none; }
  .card--logo-side .brand { font-size: 46px; }
  .card--logo-side .brand__dot { width: 26px; height: 26px; background: var(--white); }
  .socials {
    display: flex; gap: 16px; margin-top: 34px;
    font-size: 12px; font-weight: 500; list-style: none;
  }
  .socials__item { display: flex; align-items: center; gap: 6px; }
  .socials__dot { width: 12px; height: 12px; border-radius: 50%; background: var(--pink); }
  .socials__item:nth-child(2) .socials__dot { background: #3fa7e6; }
  .socials__item:nth-child(3) .socials__dot { background: var(--purple); border: 1px solid var(--white); }
  .site { margin-top: 18px; font-size: 14px; letter-spacing: .5px; }

  /* Details side */
  .card--details-side {
    left: 580px; top: 520px;
    background: var(--white);
  }
  .card--details-side .brand {
    position: absolute; left: 30px; top: 108px;
    font-size: 27px; color: var(--navy); letter-spacing: 2px; gap: 9px;
  }
  .card--details-side .brand__dot { width: 16px; height: 16px; background: var(--pink); }
  .divider {
    position: absolute; left: 250px; top: 30px;
    width: 2px; height: 160px; background: var(--pink);
  }
  .details { position: absolute; left: 266px; top: 26px; color: var(--ink); font-size: 12px; line-height: 1.4; }
  .details__name { color: var(--pink); font-weight: 700; font-size: 21px; letter-spacing: .5px; line-height: 1.1; }
  .details__role { font-size: 13px; margin-bottom: 10px; }
  .details__company { color: var(--pink); font-weight: 600; font-size: 13px; }
  .details__address { margin-bottom: 8px; }
  .contact { list-style: none; }
  .contact li { display: flex; align-items: center; gap: 8px; }
  .contact svg { width: 12px; height: 12px; flex: none; fill: var(--pink); }
  .wave { position: absolute; left: 0; top: 0; width: 560px; height: 320px; }
</style>
</head>
<body>

<section class="card card--logo-side">
  <div class="brand"><span class="brand__dot"></span>HALVARD</div>
  <ul class="socials">
    <li class="socials__item"><span class="socials__dot"></span>Pagebloom</li>
    <li class="socials__item"><span class="socials__dot"></span>Quibbly</li>
    <li class="socials__item"><span class="socials__dot"></span>Snapverse</li>
  </ul>
  <p class="site">www.halvardexperience.example</p>
</section>

<section class="card card--details-side">
  <svg class="wave" viewBox="0 0 560 320" aria-hidden="true">
    <path d="M0 320 L0 308 C140 262 300 270 420 248 C480 237 530 226 560 218 L560 320 Z" fill="var(--pink)"/>
    <path d="M0 298 C140 252 300 260 420 238 C480 227 530 216 560 208" fill="none" stroke="var(--purple)" stroke-width="4"/>
  </svg>
  <div class="brand"><span class="brand__dot"></span>HALVARD</div>
  <div class="divider"></div>
  <div class="details">
    <p class="details__name">MAREN DOYLE</p>
    <p class="details__role">Business Development Manager</p>
    <p class="details__company">HALVARD GROUP,</p>
    <p class="details__address">48 Fenwick Row Kilwinning,<br>Ayrshire, Scotland KB27 4RT</p>
    <ul class="contact">
      <li><svg viewBox="0 0 24 24"><path d="M6.6 10.8a15 15 0 0 0 6.6 6.6l2.2-2.2c.3-.3.7-.4 1-.2 1.1.4 2.3.6 3.6.6.6 0 1 .4 1 1V20c0 .6-.4 1-1 1A17 17 0 0 1 3 4c0-.6.4-1 1-1h3.5c.6 0 1 .4 1 1 0 1.3.2 2.5.6 3.6.1.3 0 .7-.2 1z"/></svg>+44 (0)1632 960418</li>
      <li><svg viewBox="0 0 24 24"><path d="M2 5h20v14H2z"/><path d="M3 6l9 7 9-7v-.5H3z" fill="#fff"/></svg>marendoyle@halvardtravel.example</li>
      <li><svg viewBox="0 0 24 24"><path d="M12 2a10 10 0 1 0 0 20 10 10 0 0 0 0-20zm0 2c.9 1.2 1.6 2.6 2 4h-4c.4-1.4 1.1-2.8 2-4zM4.3 14a8 8 0 0 1 0-4h3.4a16 16 0 0 0 0 4zm1 2h3c.3 1.3.8 2.5 1.4 3.6A8 8 0 0 1 5.3 16zm3-8h-3a8 8 0 0 1 4.4-3.6C9.1 5.5 8.6 6.7 8.3 8zM12 20c-.9-1.2-1.6-2.6-2-4h4c-.4 1.4-1.1 2.8-2 4zm2.3-6H9.7a14 14 0 0 1 0-4h4.6a14 14 0 0 1 0 4zm.3 5.6c.6-1.1 1.1-2.3 1.4-3.6h3a8 8 0 0 1-4.4 3.6zM16.3 14a16 16 0 0 0 0-4h3.4a8 8 0 0 1 0 4z"/></svg>www.halvardtravel.example</li>
    </ul>
  </div>
</section>

</body>
</html>
```